Business Card Design Competition

We need a business card design for our Internet Marketing company. We require both front and back designs and the final card must be 89x53mm in size, plus crop marks to 91x55mm. Colours as per logo, plus perhaps black and/or grey (#828282).
Final text must be editable (if you can supply an editable Fireworks PNG, even better)...
FRONT TEXT:
Full Name
Position
Address Line
Suburb, State, Postcode
Phone: 0000 000 000
Mobile: 0000 000 000
Email: xxx@brimleafpromo.com.au
Web: www.brimleafpromo.com.au
Rear of card should be a fresh design plus our slogan text: "Getting You Noticed" in large font, then in small text "Brimleaf Holdings Pty Ltd (ABN: 42 563 701 384)".
Target Market(s)
Small/Medium Businesses
Industry/Entity Type
Business
Look and feel
Each slider illustrates characteristics of the customer's brand and the style your logo design should communicate.

```html
<!DOCTYPE html>
<html lang="en">
<head>
<meta charset="utf-8">
<title>Brimleaf Promo – Business Card</title>
<link rel="stylesheet" href="https://fonts.googleapis.com/css2?family=Arimo:wght@700&display=swap">
<style>
  :root {
    --paper: #ffffff;
    --ink: #111111;
    --brand-orange: #f7a12f;
    --brand-green: #8cc63f;
    --crop: #888888;
  }
  html, body {
    margin: 0;
    padding: 0;
    overflow: hidden;
    background: var(--paper);
  }
  .sheet {
    position: relative;
    width: 1200px;
    height: 427px;
    background: var(--paper);
    font-family: "Arimo", Arial, sans-serif;
    font-weight: 700;
    color: var(--ink);
    overflow: hidden;
  }
  .crop-marks {
    position: absolute;
    inset: 0;
  }
  .crop-marks line {
    stroke: var(--crop);
    stroke-width: 1;
  }

  /* Rear side */
  .card-rear {
    position: absolute;
    left: 87px;
    top: 87px;
    width: 416px;
    height: 252px;
  }
  .brand-lockup {
    position: absolute;
    left: 17px;
    top: 14px;
    display: flex;
    align-items: center;
    gap: 18px;
  }
  .brand-dot {
    width: 116px;
    height: 116px;
    border-radius: 50%;
    background: var(--brand-orange);
    flex: none;
  }
  .brand-name {
    color: var(--brand-green);
    font-size: 44px;
    line-height: 46px;
    letter-spacing: 1px;
  }
  .slogan {
    position: absolute;
    left: 0;
    right: 0;
    top: 166px;
    margin: 0;
    text-align: center;
    font-size: 28px;
    line-height: 34px;
  }
  .company-line {
    position: absolute;
    left: 0;
    right: 0;
    top: 209px;
    margin: 0;
    text-align: center;
    font-size: 14px;
    line-height: 18px;
  }

  /* Front side */
  .card-front {
    position: absolute;
    left: 704px;
    top: 93px;
    width: 403px;
    height: 241px;
    background: var(--brand-orange);
  }
  .contact {
    position: absolute;
    left: 16px;
    top: 13px;
    margin: 0;
    font-size: 14.5px;
    line-height: 19px;
    font-style: normal;
  }
  .contact p {
    margin: 0 0 19px;
  }
  .contact p:last-child {
    margin-bottom: 0;
  }
  .front-badge {
    position: absolute;
    right: 34px;
    top: 22px;
    width: 104px;
    height: 104px;
    border-radius: 50%;
    background: var(--paper);
    display: flex;
    align-items: center;
    justify-content: center;
    text-align: center;
    color: var(--brand-green);
    font-size: 15px;
    line-height: 18px;
  }
</style>
</head>
<body>
<main class="sheet">
  <svg class="crop-marks" width="1200" height="427" viewBox="0 0 1200 427" aria-hidden="true">
    <!-- rear side marks -->
    <line x1="87.5" y1="0" x2="87.5" y2="59"/>
    <line x1="503.5" y1="0" x2="503.5" y2="59"/>
    <line x1="87.5" y1="368" x2="87.5" y2="427"/>
    <line x1="503.5" y1="368" x2="503.5" y2="427"/>
    <line x1="0" y1="87.5" x2="59" y2="87.5"/>
    <line x1="0" y1="339.5" x2="59" y2="339.5"/>
    <line x1="531" y1="87.5" x2="589" y2="87.5"/>
    <line x1="531" y1="339.5" x2="589" y2="339.5"/>
    <!-- front side marks -->
    <line x1="698.5" y1="0" x2="698.5" y2="59"/>
    <line x1="1112.5" y1="0" x2="1112.5" y2="59"/>
    <line x1="698.5" y1="368" x2="698.5" y2="427"/>
    <line x1="1112.5" y1="368" x2="1112.5" y2="427"/>
    <line x1="613" y1="87.5" x2="668" y2="87.5"/>
    <line x1="613" y1="339.5" x2="668" y2="339.5"/>
    <line x1="1141" y1="87.5" x2="1200" y2="87.5"/>
    <line x1="1141" y1="339.5" x2="1200" y2="339.5"/>
  </svg>

  <section class="card-rear" aria-label="Card rear">
    <div class="brand-lockup">
      <span class="brand-dot" aria-hidden="true"></span>
      <span class="brand-name">Brimleaf<br>Promo</span>
    </div>
    <h1 class="slogan">Getting You Noticed</h1>
    <p class="company-line">Brimleaf Holdings Pty Ltd (ABN: 42 563 701 384)</p>
  </section>

  <section class="card-front" aria-label="Card front">
    <address class="contact">
      <p>Full Name<br>Position</p>
      <p>Address Line<br>Suburb, State, Postcode</p>
      <p>Phone: 0000 000 000<br>Mobile: 0000 000 000</p>
      <p>Email: xxx@brimleafpromo.com.au<br>Web: www.brimleafpromo.com.au</p>
    </address>
    <div class="front-badge">Brimleaf<br>Promo</div>
  </section>
</main>
</body>
</html>
```